Sign Design for Truck Repair Shop center

Need a road-side sign for a pickup truck repair shop called HaulPoint Garage. The logo is attached and should be used on the sign. The background should be white and the main part of the logo should take up a large part of the sign so it can be easily read by passing traffic. The sign is 4 feet tall by 8 feet wide. Also need to add the website address" "www.HaulPointGarage-example.com" and "Call/Text 555.382.4607"

```html
<!DOCTYPE html>
<html lang="en">
<head>
<meta charset="utf-8">
<title>HaulPoint Garage – Roadside Sign</title>
<link href="https://fonts.googleapis.com/css2?family=Roboto+Slab:wght@700&display=swap" rel="stylesheet">
<style>
  :root {
    --brand-blue: #0f55a0;
    --sign-white: #ffffff;
    --backdrop: #e6e8eb;
    --shadow: rgba(0, 0, 0, 0.28);
  }
  html, body {
    margin: 0;
    padding: 0;
    width: 1050px;
    height: 1200px;
    overflow: hidden;
    background: var(--backdrop);
  }
  .canvas {
    position: relative;
    width: 1050px;
    height: 1200px;
  }
  .sign {
    position: absolute;
    left: 25px;
    top: 350px;
    width: 1000px;
    height: 500px;
    background: var(--sign-white);
    box-shadow: 4px 4px 8px var(--shadow);
    font-family: "Roboto Slab", Georgia, serif;
    font-weight: 700;
    overflow: hidden;
  }
  .sign__lines {
    position: absolute;
    inset: 0;
  }
  .brand {
    position: absolute;
    left: 0;
    right: 0;
    top: 0;
    height: 326px;
    text-align: center;
    color: var(--brand-blue);
  }
  .brand__name {
    position: absolute;
    left: 0;
    right: 0;
    top: 62px;
    font-size: 112px;
    line-height: 1;
    letter-spacing: 1px;
    margin: 0;
  }
  .brand__sub {
    position: absolute;
    left: 0;
    right: 0;
    top: 182px;
    font-size: 46px;
    line-height: 1;
    letter-spacing: 14px;
    margin: 0;
  }
  .brand__tagline {
    position: absolute;
    left: 0;
    right: 0;
    top: 250px;
    font-size: 25px;
    line-height: 1;
    letter-spacing: 1px;
    margin: 0;
  }
  .contact {
    position: absolute;
    left: 0;
    right: 0;
    top: 350px;
    text-align: center;
    color: var(--sign-white);
    white-space: nowrap;
    text-shadow: 1px 2px 3px rgba(0, 0, 0, 0.3);
  }
  .contact__label {
    font-size: 46px;
    margin-right: 14px;
  }
  .contact__phone {
    font-size: 80px;
  }
  .website {
    position: absolute;
    left: 141px;
    top: 439px;
    width: 717px;
    height: 43px;
    background: var(--sign-white);
    color: var(--brand-blue);
    font-size: 33px;
    line-height: 43px;
    text-align: center;
    white-space: nowrap;
  }
</style>
</head>
<body>
  <div class="canvas">
    <section class="sign" aria-label="HaulPoint Garage roadside sign">
      <svg class="sign__lines" width="1000" height="500" viewBox="0 0 1000 500" aria-hidden="true">
        <defs>
          <clipPath id="upper-area"><rect x="0" y="0" width="1000" height="326"/></clipPath>
          <clipPath id="band-area"><rect x="0" y="326" width="1000" height="174"/></clipPath>
        </defs>
        <rect class="contact-band" x="0" y="326" width="1000" height="174" fill="var(--brand-blue)"/>
        <rect class="frame frame--upper" x="21" y="17" width="958" height="443" fill="none" stroke="var(--brand-blue)" stroke-width="3" clip-path="url(#upper-area)"/>
        <rect class="frame frame--band" x="21" y="17" width="958" height="443" fill="none" stroke="var(--sign-white)" stroke-width="2" clip-path="url(#band-area)"/>
      </svg>

      <div class="brand">
        <p class="brand__name">HAULPOINT</p>
        <p class="brand__sub">GARAGE</p>
        <p class="brand__tagline">YOUR TRUSTED TORVAN SPECIALISTS</p>
      </div>

      <div class="contact">
        <span class="contact__label">Call/Text</span><span class="contact__phone">555.382.4607</span>
      </div>

      <div class="website">WWW.HAULPOINTGARAGE-EXAMPLE.COM</div>
    </section>
  </div>
</body>
</html>
```